Business card design for Velvet Harbor

We need business cards designed for our new marketing consulting company, Velvet Harbor. Our services include marketing strategy, go-to-market and launch planning, growth strategy, and execution. We serve medical technology and health technology companies, from startups to well-established growth companies.

The business cards should feel professional, credible, reliable and trustworthy, and should instill confidence. Also bold, creative, and modern.

The design must use the Velvet Harbor logo.

The primary brand color is this orange: #FF5501
A secondary color that you can use is this gray: #282B2D
I would prefer only to use the orange and gray. But if you feel you really need an additional accent color (please use it very sparingly, as little as possible), you can use this blue for small accent purposes: #009FED

Attached are the logo files. The main logo is the one with a little bit of orange on the left and the rest is gray.

The business card should include the following:

Velvet Harbor logo
First name and last name
Title
Email address
Phone number and type (in whatever order looks best for the design
Website (the website does not need to be in the same block as the personal info)

For example:

Nessa Pryle
Founder & Principal
nessa@velvetharbor.com
+1.628.309.4156 mobile (can use "." or spaces in between blocks of numbers)
velvetharbor.com (somewhere on the card, it does not need to be with the personal info; and note that there is no "www." at the beginning)

Note that there will be no address listed on the business card.

Target Market(s)

Executives (CEO, head of marketing, head of sales) at medical technology and health technology companies, mostly in their 40s and older, well-educated, often with advanced degrees. They are strategic thinkers, responsible for budgets, and familiar with P&L. Their comfort with and trust in using outside consultants varies.

Industry/Entity Type

Medical technology and health technology companies.

Contact Information for Business Card

See project description

Font styles to use
Sans Serif

Requirements
Must have
• Logo and see Business card details section above.

```html
<!DOCTYPE html>
<html lang="en">
<head>
<meta charset="utf-8">
<title>Velvet Harbor — Business Card</title>
<link rel="stylesheet" href="https://fonts.googleapis.com/css2?family=Archivo:wght@400;500;600&family=Krona+One&display=swap">
<style>
  :root {
    --brand-orange: #FF5501;
    --brand-gray: #282B2D;
    --paper: #FFFFFF;
    --backdrop: #6B7276;
    --pattern-tone: #33373A;
    --text-dark: #1E2022;
  }
  * { box-sizing: border-box; margin: 0; padding: 0; }
  html, body {
    width: 1200px; height: 780px; overflow: hidden;
    background: var(--backdrop);
  }
  .sheet {
    width: 1200px; height: 780px;
    display: flex; align-items: center; justify-content: center; gap: 40px;
  }
  .card {
    position: relative;
    width: 540px; height: 308px;
    overflow: hidden;
    box-shadow: 0 10px 24px rgba(0,0,0,0.35);
  }

  /* Back side */
  .card-back { background: var(--brand-gray); }
  .card-back .pattern-area {
    position: absolute; inset: 0;
    background: linear-gradient(135deg, var(--brand-gray) 0%, var(--pattern-tone) 50%, var(--brand-gray) 100%);
  }
  .card-back .wordmark {
    position: absolute; right: 40px; top: 50%; transform: translateY(-50%);
    color: var(--paper);
  }

  /* Wordmark */
  .wordmark {
    display: flex; align-items: center; gap: 12px;
    font-family: "Krona One", "Archivo", sans-serif;
    font-size: 15px; letter-spacing: 0.14em; text-transform: uppercase;
    line-height: 1;
  }
  .wordmark-dot {
    width: 26px; height: 26px; border-radius: 50%;
    background: var(--brand-orange); flex: none;
  }

  /* Front side */
  .card-front { background: var(--paper); color: var(--text-dark); }
  .card-front .wordmark {
    position: absolute; right: 36px; top: 42px;
    color: var(--brand-gray);
  }
  .person-name {
    position: absolute; left: 36px; top: 142px;
    font-family: "Krona One", "Archivo", sans-serif;
    font-size: 25px; color: var(--brand-orange);
    text-transform: uppercase; letter-spacing: 0.02em; line-height: 1;
  }
  .person-title {
    position: absolute; left: 40px; top: 176px;
    font-family: "Archivo", sans-serif; font-weight: 500;
    font-size: 13px; text-transform: uppercase; letter-spacing: 0.01em;
    color: var(--text-dark);
  }
  .divider {
    position: absolute; left: 40px; right: 36px; top: 198px;
    height: 1px; background: var(--brand-gray);
  }
  .contact-list {
    position: absolute; left: 40px; top: 214px;
    list-style: none;
    font-family: "Archivo", sans-serif; font-size: 13px; font-weight: 500;
    color: var(--text-dark);
  }
  .contact-list li {
    display: flex; align-items: center; gap: 10px; height: 24px;
  }
  .contact-icon { width: 12px; height: 12px; fill: var(--brand-orange); flex: none; }
  .website {
    position: absolute; right: 36px; top: 244px;
    font-family: "Archivo", sans-serif; font-size: 13px; font-weight: 500;
    color: var(--text-dark);
  }
  .edge-band {
    position: absolute; left: 0; right: 0; bottom: 0; height: 10px;
    display: flex;
  }
  .edge-band-gray { width: 63%; background: var(--brand-gray); }
  .edge-band-gap { width: 4px; background: var(--paper); }
  .edge-band-orange { flex: 1; background: var(--brand-orange); }
</style>
</head>
<body>
<main class="sheet">
  <section class="card card-back" aria-label="Card back">
    <div class="pattern-area" role="img" aria-label="Faint repeating brand pattern in dark gray tones"></div>
    <div class="wordmark">
      <span class="wordmark-dot"></span>
      <span class="wordmark-name">Velvet Harbor</span>
    </div>
  </section>

  <section class="card card-front" aria-label="Card front">
    <div class="wordmark">
      <span class="wordmark-dot"></span>
      <span class="wordmark-name">Velvet Harbor</span>
    </div>

    <h1 class="person-name">Nessa Pryle</h1>
    <p class="person-title">Founder &amp; Principal</p>
    <div class="divider"></div>

    <ul class="contact-list">
      <li>
        <svg class="contact-icon" viewBox="0 0 24 24" aria-hidden="true"><path d="M6.6 10.8a15.1 15.1 0 0 0 6.6 6.6l2.2-2.2a1 1 0 0 1 1-.25 11.4 11.4 0 0 0 3.6.57 1 1 0 0 1 1 1V20a1 1 0 0 1-1 1A17 17 0 0 1 3 4a1 1 0 0 1 1-1h3.5a1 1 0 0 1 1 1c0 1.25.2 2.45.57 3.57a1 1 0 0 1-.25 1z"/></svg>
        <span>+1.628.309.4156</span>
      </li>
      <li>
        <svg class="contact-icon" viewBox="0 0 24 24" aria-hidden="true"><path d="M2 5h20v14H2z M2 5l10 8 10-8" fill="none" stroke="#FF5501" stroke-width="2.5"/></svg>
        <span>nessa@velvetharbor.com</span>
      </li>
    </ul>

    <p class="website">velvetharbor.com</p>

    <div class="edge-band">
      <span class="edge-band-gray"></span>
      <span class="edge-band-gap"></span>
      <span class="edge-band-orange"></span>
    </div>
  </section>
</main>
</body>
</html>
```